Flyer

I am a qualified accountant and I need a flyer to promote my business when networking

My services include
Management Accounts, Financial Accounts, Day to Day Bookkeeping services, business start up assistance
I will produce and submit Self Assessment Tax Returns, Annual Accounts, VAT tax returns, Payroll and PAYE

I attach my business card design so that there is some continuity if you think it appropiate.

Size A3 is preferred, please.

Sorry, I mean't Size A5 is preferred.

A5 please

Free initial consultations and advice.                                   

Business

```html
<!DOCTYPE html>
<html lang="en">
<head>
<meta charset="utf-8">
<title>Clara Webb Accounting – Flyer</title>
<link href="https://fonts.googleapis.com/css2?family=Open+Sans:wght@400;600&family=Roboto+Slab:wght@300;400;700&display=swap" rel="stylesheet">
<style>
  :root{
    --page:#e8e9ea;
    --paper:#ffffff;
    --green:#a8c733;
    --charcoal:#323335;
    --ink:#4a4b4d;
    --band:#dcdfd0;
    --photo-cool:#8ea2b2;
    --photo-dark:#3a3f4c;
    --photo-warm:#c4c2ae;
  }
  *{box-sizing:border-box;margin:0;padding:0}
  html,body{width:1200px;height:1000px;overflow:hidden;background:var(--page)}
  .flyer{position:absolute;left:267px;top:30px;width:666px;height:940px;background:var(--paper);overflow:hidden;box-shadow:0 2px 10px rgba(0,0,0,.15)}
  .flyer__photo{position:absolute;left:0;top:150px;width:666px;height:390px;
    background:linear-gradient(100deg,var(--photo-cool) 0%,#6f7f90 25%,var(--photo-dark) 50%,#2f3440 65%,var(--photo-warm) 100%)}
  .flyer__shapes{position:absolute;left:0;top:0}
  .brand{position:absolute;top:62px;left:0;width:100%;text-align:center;color:var(--ink)}
  .brand__name{font-family:"Roboto Slab",serif;font-weight:400;font-size:30px;letter-spacing:1px;text-transform:uppercase}
  .brand__tagline{font-family:"Open Sans",sans-serif;font-size:14px;margin-top:4px}
  .headline{position:absolute;top:536px;left:0;width:100%;text-align:center;color:#fff;font-family:"Roboto Slab",serif;font-size:30px;font-weight:300;letter-spacing:.5px}
  .headline strong{font-weight:700}
  .services{position:absolute;top:640px;list-style:none;font-family:"Open Sans",sans-serif;font-size:15.5px;color:var(--ink);line-height:1.25}
  .services--left{left:48px;width:220px}
  .services--right{left:400px;width:230px}
  .services li{position:relative;padding-left:28px;margin-bottom:16px}
  .services li svg{position:absolute;left:0;top:1px}
  .centre-mark{position:absolute;left:313px;top:705px;width:40px;height:40px;border:2px solid var(--ink);border-radius:50%}
  .offer{position:absolute;top:848px;left:0;width:100%;height:44px;line-height:44px;text-align:center;font-family:"Roboto Slab",serif;font-size:20px;color:var(--ink)}
  .offer strong{font-weight:700}
  .contact{position:absolute;top:892px;left:0;width:100%;height:48px;display:flex;align-items:center;font-family:"Open Sans",sans-serif;font-size:17px;color:#fff}
  .contact__item{display:flex;align-items:center;gap:12px;position:absolute}
  .contact__item--email{left:56px}
  .contact__item--phone{left:410px}
</style>
</head>
<body>
<main class="flyer">
  <div class="flyer__photo" role="img" aria-label="Photo of a businessman in a suit pointing at a rising growth arrow over a city skyline"></div>

  <svg class="flyer__shapes" width="666" height="940" viewBox="0 0 666 940" aria-hidden="true">
    <rect x="0" y="0" width="666" height="10" fill="var(--green)"/>
    <path d="M0,140 L666,140 L666,178 Q330,232 0,200 Z" fill="var(--paper)"/>
    <path d="M0,524 Q330,488 666,512 L666,600 Q390,640 0,612 Z" fill="var(--green)"/>
    <path d="M0,612 Q390,640 666,600 L666,620 L0,620 Z" fill="var(--paper)"/>
    <rect x="0" y="848" width="666" height="44" fill="var(--band)"/>
    <rect x="0" y="892" width="666" height="48" fill="var(--charcoal)"/>
  </svg>

  <header class="brand">
    <div class="brand__name">Clara Webb Accounting</div>
    <div class="brand__tagline">Making Accounts look easy</div>
  </header>

  <h1 class="headline">MAKING ACCOUNTS <strong>LOOK EASY</strong></h1>

  <ul class="services services--left">
    <li><svg width="17" height="17" viewBox="0 0 17 17"><circle cx="8.5" cy="8.5" r="7.5" fill="none" stroke="var(--green)" stroke-width="1.6"/><path d="M5 8.8l2.5 2.4L12 6.2" fill="none" stroke="var(--green)" stroke-width="1.8"/></svg>Management Accounting</li>
    <li><svg width="17" height="17" viewBox="0 0 17 17"><circle cx="8.5" cy="8.5" r="7.5" fill="none" stroke="var(--green)" stroke-width="1.6"/><path d="M5 8.8l2.5 2.4L12 6.2" fill="none" stroke="var(--green)" stroke-width="1.8"/></svg>Financial Accounting</li>
    <li><svg width="17" height="17" viewBox="0 0 17 17"><circle cx="8.5" cy="8.5" r="7.5" fill="none" stroke="var(--green)" stroke-width="1.6"/><path d="M5 8.8l2.5 2.4L12 6.2" fill="none" stroke="var(--green)" stroke-width="1.8"/></svg>Day to Day<br>Bookkeeping Services</li>
    <li><svg width="17" height="17" viewBox="0 0 17 17"><circle cx="8.5" cy="8.5" r="7.5" fill="none" stroke="var(--green)" stroke-width="1.6"/><path d="M5 8.8l2.5 2.4L12 6.2" fill="none" stroke="var(--green)" stroke-width="1.8"/></svg>Business start up<br>assistance</li>
  </ul>

  <div class="centre-mark" aria-hidden="true"></div>

  <ul class="services services--right">
    <li><svg width="17" height="17" viewBox="0 0 17 17"><circle cx="8.5" cy="8.5" r="7.5" fill="none" stroke="var(--green)" stroke-width="1.6"/><path d="M5 8.8l2.5 2.4L12 6.2" fill="none" stroke="var(--green)" stroke-width="1.8"/></svg>Production and<br>submission of Self<br>Assessment Tax Returns</li>
    <li><svg width="17" height="17" viewBox="0 0 17 17"><circle cx="8.5" cy="8.5" r="7.5" fill="none" stroke="var(--green)" stroke-width="1.6"/><path d="M5 8.8l2.5 2.4L12 6.2" fill="none" stroke="var(--green)" stroke-width="1.8"/></svg>Annual Accounts</li>
    <li><svg width="17" height="17" viewBox="0 0 17 17"><circle cx="8.5" cy="8.5" r="7.5" fill="none" stroke="var(--green)" stroke-width="1.6"/><path d="M5 8.8l2.5 2.4L12 6.2" fill="none" stroke="var(--green)" stroke-width="1.8"/></svg>VAT tax returns</li>
    <li><svg width="17" height="17" viewBox="0 0 17 17"><circle cx="8.5" cy="8.5" r="7.5" fill="none" stroke="var(--green)" stroke-width="1.6"/><path d="M5 8.8l2.5 2.4L12 6.2" fill="none" stroke="var(--green)" stroke-width="1.8"/></svg>Payroll and PAYE</li>
  </ul>

  <p class="offer"><strong>FREE</strong> initial consultations and advice</p>

  <footer class="contact">
    <span class="contact__item contact__item--email">
      <svg width="26" height="18" viewBox="0 0 26 18" aria-hidden="true"><rect x="0" y="0" width="26" height="18" fill="var(--green)"/><path d="M1 1l12 9 12-9" fill="none" stroke="var(--charcoal)" stroke-width="2"/></svg>
      clara@clarawebbaccounting.com
    </span>
    <span class="contact__item contact__item--phone">
      <svg width="16" height="28" viewBox="0 0 16 28" aria-hidden="true"><rect x="0" y="0" width="16" height="28" rx="2" fill="var(--green)"/><rect x="3" y="3" width="10" height="8" fill="var(--charcoal)"/><g fill="var(--charcoal)"><rect x="3" y="14" width="2.5" height="2"/><rect x="6.75" y="14" width="2.5" height="2"/><rect x="10.5" y="14" width="2.5" height="2"/><rect x="3" y="18" width="2.5" height="2"/><rect x="6.75" y="18" width="2.5" height="2"/><rect x="10.5" y="18" width="2.5" height="2"/><rect x="3" y="22" width="2.5" height="2"/><rect x="6.75" y="22" width="2.5" height="2"/><rect x="10.5" y="22" width="2.5" height="2"/></g></svg>
      07700 900412
    </span>
  </footer>
</main>
</body>
</html>
```